Velvet Comet Cocoa Bar - ComettoBars.example

Create chocolate bar packaging. I would like the packaging to have a wizard hat or wizard with hat on on the packaging. Packaging should be a matte finish with a glossy Wizard hat or wizard with hat on the packaging. The background should have little wizard hats or mushrooms that are imbedded into the matte finish that reflect when you move the packaging. Colors should be Black, dark purple, purple, blue, dark blue, white.

Target Market(s)

Mushroom Consumers

Industry/Entity Type

Mushroom Chocolates

Font styles to use
Serif
Sans Serif

Colors
0054AA
0677BA
7BADD7
CADEEF
E8F1F8
0094D4
00A9DD
6FCCEA
C7EBF8
E9F6FB
A7469A
B969AE
D3A5CF
EDDBEB
F8F0F9
6B429C
8869AF
B7A5CE
E3DAEB
F3F0F8

Requirements
Must have
• Wizard Hat
Nice to have
• Reflective small mushrooms or wizard hats in the matte background
Should not have
• to many colors

```html
<!DOCTYPE html>
<html lang="en">
<head>
<meta charset="utf-8">
<title>Velvet Comet Cocoa Bar – Packaging</title>
<link rel="stylesheet" href="https://fonts.googleapis.com/css2?family=Bowlby+One&family=Nunito:wght@600;700;800&display=swap">
<style>
  :root {
    --night: #0d0628;
    --wrapper: #140c33;
    --wrapper-glow: #2a2150;
    --violet: #8869af;
    --orchid: #a7469a;
    --royal: #6b429c;
    --blue: #4a5fae;
    --lilac: #b7a5ce;
    --mist: #d3cde6;
  }
  * { margin: 0; padding: 0; box-sizing: border-box; }
  html, body { width: 1200px; height: 792px; overflow: hidden; background: var(--night); }
  .canvas {
    position: relative;
    width: 1200px;
    height: 792px;
    background: var(--night);
    font-family: "Nunito", sans-serif;
  }

  /* Brand block */
  .brand {
    position: absolute;
    left: 40px;
    top: 110px;
    width: 470px;
    height: 540px;
    display: flex;
    flex-direction: column;
    align-items: center;
    justify-content: center;
    gap: 34px;
  }
  .brand-dot {
    width: 150px;
    height: 150px;
    border-radius: 50%;
    background: var(--royal);
  }
  .brand-name {
    font-family: "Bowlby One", sans-serif;
    font-weight: 400;
    font-size: 66px;
    line-height: 1.02;
    text-align: center;
    color: var(--violet);
    text-transform: uppercase;
  }

  /* Packs */
  .pack {
    position: absolute;
    top: 62px;
    width: 270px;
    height: 636px;
    background: radial-gradient(ellipse at 50% 25%, var(--wrapper-glow) 0%, var(--wrapper) 60%);
    display: flex;
    flex-direction: column;
    align-items: center;
  }
  .pack--front { left: 548px; }
  .pack--back  { left: 872px; }

  .pack-seal {
    width: 100%;
    height: 38px;
    background:
      repeating-linear-gradient(180deg, rgba(255,255,255,0.08) 0 2px, transparent 2px 5px),
      linear-gradient(90deg, var(--blue), var(--royal) 55%, var(--orchid));
  }
  .pack-body {
    flex: 1;
    width: 100%;
    display: flex;
    flex-direction: column;
    align-items: center;
    padding: 70px 22px 0;
  }
  .pack-name {
    font-family: "Bowlby One", sans-serif;
    font-size: 33px;
    line-height: 1.05;
    text-align: center;
    color: var(--violet);
    text-transform: uppercase;
  }
  .pack-flavour {
    margin-top: 58px;
    font-weight: 700;
    font-size: 23px;
    color: var(--mist);
  }
  .pack-strain {
    margin-top: 4px;
    font-weight: 800;
    font-size: 17px;
    letter-spacing: 7px;
    color: var(--mist);
  }
  .pack-icon {
    margin-top: 26px;
    width: 34px;
    height: 44px;
    border-radius: 17px 17px 10px 10px;
    background: var(--lilac);
  }
  .pack-dose {
    margin-top: 52px;
    font-family: "Bowlby One", sans-serif;
    font-size: 26px;
    color: var(--lilac);
  }
  .pack-note {
    margin-top: 4px;
    font-weight: 600;
    font-size: 15px;
    line-height: 1.2;
    text-align: center;
    color: var(--lilac);
  }
</style>
</head>
<body>
<main class="canvas">

  <section class="brand">
    <div class="brand-dot"></div>
    <h1 class="brand-name">Velvet Comet<br>Cocoa Bar</h1>
  </section>

  <article class="pack pack--front">
    <div class="pack-seal"></div>
    <div class="pack-body">
      <h2 class="pack-name">Velvet Comet<br>Cocoa Bar</h2>
      <p class="pack-flavour">cookies &amp; cream</p>
      <p class="pack-strain">-ENIGMA-</p>
      <div class="pack-icon" role="img" aria-label="Small mushroom icon"></div>
      <p class="pack-dose">3.5g</p>
      <p class="pack-note">of wizard magic<br>per bar</p>
    </div>
    <div class="pack-seal"></div>
  </article>

  <article class="pack pack--back">
    <div class="pack-seal"></div>
    <div class="pack-body">
      <h2 class="pack-name">Velvet Comet<br>Cocoa Bar</h2>
      <p class="pack-flavour">cookies &amp; cream</p>
      <p class="pack-strain">-ENIGMA-</p>
      <div class="pack-icon" role="img" aria-label="Small mushroom icon"></div>
      <p class="pack-dose">3.5g</p>
      <p class="pack-note">of wizard magic<br>per bar</p>
    </div>
    <div class="pack-seal"></div>
  </article>

</main>
</body>
</html>
```